My company is throwing a party. The name is 70/30 (70% Reggae & 30% Whatever Comes)

I seek a flyer that shows this will be a very elegant, upscale event and at the same time high energy, great reggae music and dancing.

I need this flyer to be 650 pixels wide & any length, High resolution (1MB) for printing on a 4" x 6" flyer.

Target Market(s)

Fans of reggae music

Industry/Entity Type

Printing

Requirements
Must have
• Lumen Harbor Holdings Presents:
70/30
Upscale Reggae Soiree
70% Reggae - 30% Whatever Comes

Saturday May 4th, 10pm - 3am

The Copperloft: 418 1/2 North Callow St, OKC

Dress to impress! We reserve the right to refuse entry

Free Entry: 1st 50 Ladies On VIP Guestlist - Discounted Early Bird Online Tickets - For Bottle Service Reservation: http://islandnights.ticketvoro.com

More info? 405-617-2958

```html
<!DOCTYPE html>
<html lang="en">
<head>
<meta charset="utf-8">
<title>70/30 — Upscale Reggae Soiree</title>
<link href="https://fonts.googleapis.com/css2?family=Bebas+Neue&family=Montserrat:wght@400;700;800&display=swap" rel="stylesheet">
<style>
  :root {
    --ink: #000000;
    --band: #0a0a0a;
    --white: #ffffff;
    --yellow: #f5ea1c;
    --ghost: #2f2a12;
    --green: #1fa64a;
    --lime: #b8d82a;
    --sky: #2aa6d8;
  }
  * { margin: 0; padding: 0; box-sizing: border-box; }
  html, body { width: 800px; height: 1200px; overflow: hidden; background: var(--ink); }
  .flyer {
    position: relative;
    width: 800px;
    height: 1200px;
    overflow: hidden;
    background: var(--ink);
    font-family: "Montserrat", Arial, sans-serif;
    color: var(--white);
  }
  .party-scene {
    position: absolute;
    inset: 0 0 auto 0;
    height: 470px;
    background:
      linear-gradient(180deg, rgba(0,0,0,0) 0%, rgba(0,0,0,0) 45%, rgba(0,0,0,0.85) 75%, var(--ink) 100%),
      radial-gradient(ellipse at 30% 30%, #f0e63a 0%, rgba(240,230,58,0) 35%),
      radial-gradient(ellipse at 55% 25%, var(--green) 0%, rgba(31,166,74,0) 45%),
      radial-gradient(ellipse at 85% 30%, var(--sky) 0%, rgba(42,166,216,0) 45%),
      linear-gradient(90deg, #0d3a14 0%, var(--lime) 25%, var(--green) 55%, #1a7fa8 85%, #0b2b3a 100%);
  }
  .ghost-numerals {
    position: absolute;
    left: 50%;
    top: 370px;
    transform: translateX(-50%) scaleX(0.62);
    font-family: "Bebas Neue", Impact, sans-serif;
    font-size: 540px;
    line-height: 1;
    color: var(--ghost);
    opacity: 0.75;
    white-space: nowrap;
  }
  .presenter {
    position: absolute;
    top: 400px;
    left: 0;
    width: 100%;
    display: flex;
    justify-content: center;
    align-items: center;
    gap: 12px;
    font-weight: 700;
    font-size: 20px;
    letter-spacing: 0.5px;
  }
  .presenter-dot {
    width: 18px; height: 18px; border-radius: 50%;
    background: var(--white);
  }
  .title-numerals {
    position: absolute;
    left: 50%;
    top: 462px;
    transform: translateX(-50%) scaleX(0.6);
    font-family: "Bebas Neue", Impact, sans-serif;
    font-size: 320px;
    font-weight: 400;
    line-height: 1;
    color: var(--yellow);
    white-space: nowrap;
  }
  .headline {
    position: absolute;
    top: 752px;
    width: 100%;
    text-align: center;
    font-weight: 800;
    font-size: 34px;
  }
  .mix-line {
    position: absolute;
    top: 804px;
    width: 100%;
    text-align: center;
    font-size: 24px;
  }
  .mix-line strong { color: var(--yellow); font-weight: 800; }
  .event-time {
    position: absolute;
    top: 846px;
    width: 100%;
    text-align: center;
    font-size: 22px;
    font-weight: 700;
  }
  .dress-code {
    position: absolute;
    top: 893px;
    width: 100%;
    text-align: center;
    font-size: 23px;
  }
  .dress-code strong { font-weight: 800; }
  .info-band {
    position: absolute;
    top: 940px;
    left: 0;
    width: 100%;
    height: 260px;
    background: var(--band);
  }
  .ticket-info {
    position: absolute;
    top: 962px;
    left: 24px;
    right: 24px;
    text-align: center;
    font-size: 22px;
    line-height: 41px;
  }
  .ticket-info strong { font-weight: 800; }
  .ticket-info sup { font-size: 12px; }
  .ticket-info .sep { color: var(--yellow); }
  .ticket-info .url { font-style: italic; }
  .contact {
    position: absolute;
    top: 1125px;
    display: flex;
    align-items: center;
    gap: 10px;
    font-size: 20px;
    white-space: nowrap;
  }
  .contact-address { left: 36px; }
  .contact-phone { right: 36px; }
  .contact svg { fill: var(--white); flex: none; }
</style>
</head>
<body>
<main class="flyer">
  <div class="party-scene" role="img" aria-label="Dancing crowd silhouettes with raised hands under palm trees and colourful disco lights"></div>

  <div class="ghost-numerals" aria-hidden="true">70/30</div>

  <div class="presenter"><span class="presenter-dot"></span><span>Lumen Harbor Holdings Presents:</span></div>

  <h1 class="title-numerals">70/30</h1>

  <h2 class="headline">Upscale Reggae Soiree</h2>
  <p class="mix-line"><strong>70%</strong> Reggae - <strong>30%</strong> Whatever Comes</p>
  <p class="event-time">Saturday May 4th, 10pm - 3am</p>

  <p class="dress-code"><strong>Dress to impress!</strong> We reserve the right to refuse entry</p>

  <div class="info-band"></div>
  <p class="ticket-info">
    <strong>Free Entry:</strong> 1<sup>st</sup> 50 Ladies On VIP Guestlist <span class="sep">&#9830;</span> Discounted<br>
    Early Bird Online Tickets <span class="sep">&#9830;</span> For Bottle Service Reservation:<br>
    <span class="url">http://islandnights.ticketvoro.com</span>
  </p>

  <div class="contact contact-address">
    <svg width="24" height="34" viewBox="0 0 24 34" aria-hidden="true"><path d="M12 0C5.4 0 0 5.3 0 11.9 0 20.5 12 34 12 34s12-13.5 12-22.1C24 5.3 18.6 0 12 0zm0 17a5 5 0 1 1 0-10 5 5 0 0 1 0 10z"/></svg>
    <span>The Copperloft: 418 1/2 North Callow St, OKC</span>
  </div>
  <div class="contact contact-phone">
    <svg width="30" height="32" viewBox="0 0 24 24" aria-hidden="true"><path d="M6.6 10.8a15.2 15.2 0 0 0 6.6 6.6l2.2-2.2a1 1 0 0 1 1-.25 11.4 11.4 0 0 0 3.6.57 1 1 0 0 1 1 1V20a1 1 0 0 1-1 1A17 17 0 0 1 3 4a1 1 0 0 1 1-1h3.5a1 1 0 0 1 1 1c0 1.25.2 2.45.57 3.57a1 1 0 0 1-.25 1z"/></svg>
    <span>405-617-2958</span>
  </div>
</main>
</body>
</html>
```